Chiropractic healthcare group business card

We are a Portland Oregon based chiropractic healthcare group. Looking for a new business card design. Something cutting edge, that shows off our new logo and tag line.Use either of the attached logos.Our tag line = "What could you do free of pain?"I'm open to about anything, impress me!!
Target Market(s)
Chiropractic patients - Auto injury, back pain, sports injuries, neck , shoulder, hip, knee, ankle pain.
Industry/Entity Type
Chiropractic
Contact Information for Business Card
Dr. Bram Holtvick, D.C.
Clinic name - Fernway Chiropractic
2 clinics
location #1
20418 NW Marwick Road
Suite B
North Plains, OR 97133
Location #2
13529 SE Calloway Street
Portland OR 97299
Main phone line 971.555.0143
website : www.FernwayClinics.example
Tag line "What could you do free of pain?"
Colors
Designer to choose colors to be used in the design.
Requirements
Must have
- Use the logo colors -- Want the orange color to be a TRUE orange.
- Both clinic address
- phone number
- website
- personal email - b.holtvick@ReliefBeginsHere.example
- tag line - "What could you do free of pain?"

```html
<!DOCTYPE html>
<html lang="en">
<head>
<meta charset="utf-8">
<title>Fernway Chiropractic – Business Card</title>
<link rel="stylesheet" href="https://fonts.googleapis.com/css2?family=Montserrat:wght@500;600;700&family=Roboto:wght@400;500&display=swap">
<style>
  :root {
    --backdrop: #e08a2c;
    --slate: #585858;
    --slate-dark: #434343;
    --paper: #e6e7e9;
    --orange: #f7941d;
    --ink: #4a4a4a;
    --white: #ffffff;
  }
  * { box-sizing: border-box; margin: 0; padding: 0; }
  html, body { width: 1200px; height: 1200px; overflow: hidden; }
  body {
    background: var(--backdrop);
    font-family: "Roboto", Arial, sans-serif;
    position: relative;
  }
  .card {
    position: absolute;
    left: 180px;
    width: 840px;
    height: 480px;
    background: var(--paper);
    border-radius: 6px;
    overflow: hidden;
    box-shadow: 0 12px 30px rgba(0,0,0,0.22);
  }
  .card--brand { top: 70px; }
  .card--contact { top: 650px; }

  /* Brand side */
  .band {
    position: absolute;
    left: 0;
    width: 100%;
    height: 110px;
    background: var(--slate);
  }
  .band--top { top: 0; }
  .band--bottom { bottom: 0; }
  .pill {
    position: absolute;
    left: 50%;
    transform: translateX(-50%);
    width: 560px;
    height: 48px;
    border-radius: 22px;
    background: var(--slate-dark);
  }
  .pill--top { top: 86px; }
  .pill--bottom {
    bottom: 86px;
    display: flex;
    align-items: center;
    justify-content: center;
    color: var(--white);
    font-size: 21px;
    font-style: italic;
  }
  .brand-name {
    position: absolute;
    top: 185px;
    left: 0;
    width: 100%;
    display: flex;
    align-items: center;
    justify-content: center;
    gap: 18px;
    font-family: "Montserrat", Arial, sans-serif;
    font-weight: 700;
    font-size: 44px;
    letter-spacing: 5px;
    color: var(--ink);
    text-transform: uppercase;
  }
  .brand-dot {
    width: 26px;
    height: 26px;
    border-radius: 50%;
    background: var(--orange);
    flex: none;
  }
  .website {
    position: absolute;
    bottom: 34px;
    left: 0;
    width: 100%;
    text-align: center;
    color: var(--white);
    font-size: 24px;
    letter-spacing: 0.5px;
  }

  /* Contact side */
  .chevron { position: absolute; top: 0; left: 0; }
  .brand-name--light {
    position: absolute;
    top: 180px;
    left: 22px;
    width: 300px;
    font-family: "Montserrat", Arial, sans-serif;
    font-weight: 700;
    font-size: 28px;
    letter-spacing: 3px;
    line-height: 1.35;
    color: var(--white);
    text-transform: uppercase;
  }
  .doctor {
    position: absolute;
    top: 40px;
    right: 44px;
    text-align: right;
    font-family: "Montserrat", Arial, sans-serif;
    font-weight: 500;
    font-size: 30px;
    letter-spacing: 2px;
    color: var(--ink);
    line-height: 1.25;
  }
  .contact-list {
    position: absolute;
    right: 40px;
    bottom: 40px;
    list-style: none;
    text-align: right;
    color: var(--ink);
    font-size: 19px;
    line-height: 1.3;
  }
  .contact-item {
    display: flex;
    justify-content: flex-end;
    align-items: flex-start;
    gap: 14px;
    margin-top: 12px;
  }
  .contact-icon {
    width: 24px;
    height: 24px;
    flex: none;
    margin-top: 1px;
  }
</style>
</head>
<body>

<section class="card card--brand" aria-label="Card front">
  <div class="band band--top"></div>
  <div class="pill pill--top"></div>
  <div class="band band--bottom"></div>
  <div class="pill pill--bottom">“What could you do free of pain?”</div>
  <div class="brand-name"><span class="brand-dot"></span>Fernway Chiropractic</div>
  <p class="website">www.FernwayClinics.example</p>
</section>

<section class="card card--contact" aria-label="Card back">
  <svg class="chevron" width="840" height="480" viewBox="0 0 840 480" aria-hidden="true">
    <path d="M0 0 H270 L360 200 Q380 240 360 280 L270 480 H0 Z" fill="#f7941d"/>
    <path d="M0 0 H256 L344 200 Q362 240 344 280 L256 480 H0 Z" fill="#585858"/>
  </svg>
  <div class="brand-name--light">Fernway<br>Chiropractic</div>

  <div class="doctor">DR. BRAM HOLTVICK<br>D.C</div>

  <ul class="contact-list">
    <li class="contact-item">
      <span>971.555.0143</span>
      <svg class="contact-icon" viewBox="0 0 24 24" aria-hidden="true"><circle cx="12" cy="12" r="12" fill="#434343"/><path d="M8.5 6.5l2 2-1.2 1.6c.7 1.6 2 2.9 3.6 3.6l1.6-1.2 2 2-1.4 1.6c-3.8-.5-7.1-3.8-7.6-7.6z" fill="#fff"/></svg>
    </li>
    <li class="contact-item">
      <span>b.holtvick@ReliefBeginsHere.example</span>
      <svg class="contact-icon" viewBox="0 0 24 24" aria-hidden="true"><circle cx="12" cy="12" r="12" fill="#434343"/><rect x="6.5" y="8" width="11" height="8" rx="1" fill="none" stroke="#fff" stroke-width="1.4"/><path d="M6.8 8.4l5.2 4 5.2-4" fill="none" stroke="#fff" stroke-width="1.4"/></svg>
    </li>
    <li class="contact-item">
      <span>20418 NW Marwick Road<br>Suite D, Alder Flats, OR 97450</span>
      <svg class="contact-icon" viewBox="0 0 24 24" aria-hidden="true"><circle cx="12" cy="12" r="12" fill="#434343"/><path d="M12 5.5a4 4 0 0 0-4 4c0 3 4 8 4 8s4-5 4-8a4 4 0 0 0-4-4z" fill="#fff"/><circle cx="12" cy="9.5" r="1.5" fill="#434343"/></svg>
    </li>
    <li class="contact-item">
      <span>13529 SE Calloway Street<br>Portland OR 97299</span>
      <svg class="contact-icon" viewBox="0 0 24 24" aria-hidden="true"><circle cx="12" cy="12" r="12" fill="#434343"/><path d="M12 5.5a4 4 0 0 0-4 4c0 3 4 8 4 8s4-5 4-8a4 4 0 0 0-4-4z" fill="#fff"/><circle cx="12" cy="9.5" r="1.5" fill="#434343"/></svg>
    </li>
  </ul>
</section>

</body>
</html>
```